依頼概要
◆本のタイトル
港町グラス日記~灯りの奥のササヤキ~

◆著者
桑原 美津江

◆依頼目的/概要
電子書籍を出版しますので、表紙デザイン作成をお願いいたします。

◆デザイン要望
基本的にお任せです。
イラストや写真等素材を使用される場合には、
商用利用可の素材をお願いします。

色合い、デザイン、レイアウトともデザイナーさんにお任せしたいと思います。

※参考として書籍の原稿を添付します。

◆本の内容
ショットバー”ブルクハルモン”のオーナーバーテンダーである私、桑原美津江が実話をもとに店で繰り広げられる様々な人間ドラマを本にしました。
登場人物であるお客様をヒーロー、ヒロインにするつもりで構成しました。
読者が元気や活力を得て、人生を前向きに生きる一助になることを願い、書き進めました。バーという非日常の空間の中で、臨場感や私とお客様とのやりとりがダイレクトに伝わり、読者の様々な感情を揺さぶることができれば、嬉しく思います。

◆読者ターゲット層
〇30代、40代、50代前半までの働く男性、女性
〇自分の生き方や仕事に漠然とした不安や悩みがある人
〇人生を前向きに自分らしく生きたい人
〇職場間、夫婦間、親子間など人間関係にストレスや問題を抱えている人

◆デザイン要望
〇私が女性バーテンダーで、女性のご来店も多いので、女性が一人でも行ってみたいと思わせる雰囲気のデザイン希望です

〇バーというと敷居が高く、入りにくいイメージを持っている人が多いので、品位は保ちつつもあたたかい雰囲気が伝わるようにしていただきたいです

◆写真素材購入の際は別途写真代をお支払いします。その場合は電子書籍ですので、小サイズで結構です。

◆選定確約です。

◆選定デザインの他に、次点、次々点の方にも報酬をご用意しています。

◆その他、デザインに必要な情報がありましたら、お答えします。
遠慮なく聞いてください。
お盆中で、デザイナーさんから締め切り延長のご希望がありましたので、
2日間だけ、延長することになりました。よろしくお願いします。
■ 選んだ理由

赤、黒、白のデザインは、店と私の雰囲気にぴったりで、とても気に入りました。
オビも読者目線で考えていただき、感謝しています。
おしゃれで元気にもになるそんなデザインに感じました。

■ 提案者全員のお礼・コメント

原稿を読んでくださり、それぞれの強い思いでデザインを考えてくださったのが、
伝わってきました。
お一人、お一人に感謝申し上げます。
良いデザインばかりで、選ぶのに正直とても迷いました。
出版の機会がありましたら、またコンペにご参加くださるとありがたいです。
本当にありがとうございました。

```html
<!DOCTYPE html>
<html lang="ja">
<head>
<meta charset="utf-8">
<title>港町グラス日記 〜灯りの奥のササヤキ〜</title>
<link rel="stylesheet" href="https://fonts.googleapis.com/css2?family=Noto+Sans+JP:wght@400;500&display=swap">
<style>
  :root {
    --bar-red: #c8161e;
    --paper-white: #ffffff;
    --ink-black: #1a1414;
  }
  * { margin: 0; padding: 0; box-sizing: border-box; }
  html, body {
    width: 851px;
    height: 1200px;
    overflow: hidden;
    background: var(--bar-red);
  }
  .cover {
    position: relative;
    width: 851px;
    height: 1200px;
    background: var(--bar-red);
    overflow: hidden;
    font-family: "Noto Sans JP", sans-serif;
  }
  .cover__moon {
    position: absolute;
    left: 0;
    top: 0;
  }
  .cover__title {
    position: absolute;
    left: 361px;
    top: 140px;
    width: 440px;
    text-align: center;
    color: var(--bar-red);
    font-weight: 500;
    font-size: 100px;
    line-height: 124px;
    letter-spacing: 2px;
  }
  .cover__subtitle {
    position: absolute;
    left: 93px;
    top: 326px;
    width: 40px;
    color: var(--bar-red);
    font-weight: 400;
    font-size: 36px;
    line-height: 39px;
    text-align: center;
  }
  .cover__subtitle span {
    display: block;
    height: 39px;
  }
  .cover__subtitle .wave {
    transform: rotate(90deg);
  }
  .cover__glasses {
    position: absolute;
    left: 213px;
    top: 628px;
    width: 552px;
    height: 222px;
    border-radius: 18px;
    background: linear-gradient(180deg, #2a2020 0%, var(--ink-black) 70%, #3a1416 100%);
  }
  .cover__author {
    position: absolute;
    left: 84px;
    top: 1030px;
    color: var(--paper-white);
    font-weight: 400;
    font-size: 46px;
    letter-spacing: 4px;
    white-space: nowrap;
  }
</style>
</head>
<body>
  <main class="cover">
    <svg class="cover__moon" width="851" height="1200" viewBox="0 0 851 1200" aria-hidden="true">
      <circle cx="425" cy="505" r="474" fill="var(--paper-white)"/>
    </svg>

    <h1 class="cover__title">港町<br>グラス<br>日記</h1>

    <p class="cover__subtitle" aria-label="〜灯りの奥のササヤキ〜">
      <span class="wave">〜</span><span>灯</span><span>り</span><span>の</span><span>奥</span><span>の</span><span>サ</span><span>サ</span><span>ヤ</span><span>キ</span><span class="wave">〜</span>
    </p>

    <div class="cover__glasses" role="img" aria-label="黒いシルエットで描かれた五つのカクテルグラスの並び、赤いフルーツとストローの飾り付き"></div>

    <p class="cover__author">桑原 美津江</p>
  </main>
</body>
</html>
```